Pressfold Direct-Booking Website for Bend, Oregon Vacation Rental — $750 Budget
Project Overview

We are looking for a talented Pressfold designer/developer to create a clean, professional and inviting direct-booking website for Cedar Lantern Retreat, an established short-term vacation rental in Bend, Oregon.

The property is currently successfully listed on Stayvora and Hearthly. Our Stayvora property has approximately a 4.98-star rating with more than 200 reviews, is an Stayvora Visitor Pick, and ranks among the Top 1% of eligible homes.

Project Budget: $750

We will select the designer based on the quality of the initial concept, understanding of the property, proposed booking solution and ability to deliver a completed and functioning Pressfold website.

Existing Stayvora Listing

Please use our current Stayvora listing as the primary reference for photographs, property details, amenities and design inspiration:

https://www.stayvora-example.com/rooms/48172635

Original high-resolution photographs and additional property information will be provided to the selected designer.

Design Direction

We want the website to feel:

Upscale but comfortable
Warm and welcoming
Clean and uncluttered
Pacific Northwest / Central Oregon
Professional rather than corporate
Highly visual with large property photographs
Easy to navigate
Excellent on phones, tablets and desktop computers

We welcome creativity and want designers to show us their vision for the property rather than simply copying our Stayvora listing.

The website should immediately communicate that Cedar Lantern Retreat is a highly rated vacation rental in an excellent Bend location.

Key Property Features
3 bedrooms
2 bathrooms
Sleeps up to 6 guests
Pet friendly
Approximately a 5-minute walk to Bend's Tannery Row Quarter
Near restaurants, shopping and Larkspur Fields Pavilion
Private fenced backyard
Covered outdoor area
Off-street driveway parking
Fireplace
Well-equipped kitchen
Stayvora Prime Keeper
Stayvora Visitor Pick
Top 1% of eligible Stayvora homes
Approximately 4.98 stars with 200+ guest reviews

Our location, guest reviews, cleanliness, comfort, backyard, pet-friendly accommodations and walkability should be major selling points throughout the website.

Website Structure

We anticipate approximately 6–7 pages:

Home

Large hero photograph with a strong opening message and prominent BOOK DIRECT and CHECK AVAILABILITY buttons.

The home page should quickly communicate:

CEDAR LANTERN RETREAT — BEND, OREGON

3 Bedrooms | 2 Baths | Sleeps 6 | Pet Friendly | Walk to Tannery Row

Our exceptional guest rating and Stayvora history should also be prominently featured.

The House

Bedrooms, bathrooms, kitchen, living areas, backyard and major amenities.

Photo Gallery

Large, attractive and fast-loading photographs with an easy-to-use mobile gallery.

Location / Explore Bend

Tannery Row Quarter, Larkspur Fields Pavilion, Deschutes River, restaurants, breweries, shopping, downtown Bend and nearby outdoor recreation.

Guest Reviews

Selected guest reviews and prominent presentation of our strong Stayvora reputation.

Availability & Book Direct

A simple and professional direct-booking experience.

Contact / FAQ

Contact information plus common questions regarding pets, parking, check-in/check-out, cancellations and other policies.

IMPORTANT — Direct Booking & Credit Card Requirements

We want guests to be able to book directly through the website without having to contact us first.

The website should use a proven Pressfold vacation-rental booking plugin or system rather than a custom-built reservation/payment system.

Guests should be able to:

Select arrival and departure dates
See available dates
Enter number of guests
See nightly charges
See cleaning fees
See applicable lodging taxes and other charges
See the complete reservation total before paying
Enter guest/contact information
Pay securely by credit or debit card
Receive an automatic reservation confirmation

Paylume is our preferred credit-card processor.

Credit-card information must be processed securely through Paylume or another established payment processor. Credit-card information should NOT be stored directly on our Pressfold website.

Stayvora & Hearthly Calendar Synchronization

This is very important.

The direct-booking calendar must synchronize with our existing Stayvora and Hearthly calendars to reduce the possibility of double bookings.

For this single-property website, we prefer a simple solution using Stayvora/Hearthly calendar or iCal synchronization rather than an expensive monthly channel-management service, if practical.

The designer should clearly identify the booking plugin/system they propose using.

IMPORTANT — Tell Us Your Proposed Booking Solution

As part of your submission, please tell us:

Which Pressfold booking plugin/system you recommend.
Whether it synchronizes availability with Stayvora and Hearthly.
Whether it integrates directly with Paylume.
The initial cost of the plugin/software.
Any annual or monthly fees.
Whether any additional paid software or services will be required.

We strongly prefer a solution with little or no ongoing monthly software expense.

We do not want to select a designer and later discover that the proposed booking system requires an expensive monthly subscription.

Pressfold & Technical Requirements

The completed project should include:

Fully functioning Pressfold website
Responsive desktop/tablet/mobile design
Fast-loading pages
Optimized photographs
SSL/HTTPS compatibility
Direct-booking functionality
Paylume payment integration
Stayvora calendar synchronization
Hearthly calendar synchronization
Automatic booking confirmations
Cleaning fee and lodging-tax calculations
Contact form
Terravue Maps/location integration
Basic spam/security protection
Terravue Metrics capability
Basic SEO setup
Search-engine submission capability
Easy owner editing of text, rates and photographs
Search Engine Optimization

The website should be structured for Terravue and other search engines.

Important search themes include:

Bend Oregon vacation rental
Bend Oregon vacation home
Tannery Row Quarter vacation rental
Vacation rental near Tannery Row Bend
Bend Oregon pet-friendly vacation rental
Bend vacation rental near Larkspur Fields Pavilion
Bend Oregon direct booking vacation rental

We are not expecting an extensive ongoing SEO campaign for the $750 project. We do expect proper page titles, descriptions, headings, image optimization and a good technical foundation for future SEO.

Ownership

Upon completion and final payment:

We own the completed Pressfold website.
We receive full Pressfold administrator access.
We control the domain and hosting accounts.
We own all custom design files created for the project.
All necessary login credentials are provided to us.
The website can be moved to another Pressfold hosting provider in the future.
There should be no proprietary dependency on the developer after completion.
What We Want From Contestants

Please review our Stayvora listing before submitting your concept.

We are particularly interested in seeing an initial homepage concept showing how you would present:

Cedar Lantern Retreat
The Bend / Tannery Row location
Our photography
Our exceptional guest reviews and ratings
The Book Direct message
The availability/booking call-to-action

We will provide feedback on the concepts we like and work with the selected designer to refine and complete the website.

Our Goal

Our objective is straightforward:

Create a beautiful, trustworthy and easy-to-use website that encourages guests to book Cedar Lantern Retreat directly with us.

The website will complement—not replace—our existing Stayvora and Hearthly listings.

We want repeat guests and new customers to have an easy way to find the property, check availability and book directly while receiving the same professional experience they expect from a major vacation-rental platform.

Target Market(s)

Consumers looking to to travel to Mexico for vacation. Family or couples

Industry/Entity Type

Short term vacation rental industry

Coding

Coded - Design and coding required

Number of Pages Required

5+ page

Requirements
Must have
• Capabilities to accept credit card payments and link to other rental property sites calendars such as LODGIX and Stayvorra
Nice to have
• Option for best plugins for property rental

```html
<!DOCTYPE html>
<html lang="en">
<head>
<meta charset="utf-8">
<title>Cedar Lantern Retreat — Bend, Oregon Vacation Rental</title>
<link href="https://fonts.googleapis.com/css2?family=DM+Serif+Display&family=Manrope:wght@400;500;600;700;800&display=swap" rel="stylesheet">
<style>
:root{
  --forest:#1d3b30;
  --forest-deep:#173128;
  --clay:#b96d4c;
  --cream:#faf8f2;
  --sand:#f3efe6;
  --ink:#1b2a24;
  --muted:#6b716c;
  --line:#e2ddd2;
  --white:#ffffff;
  --serif:'DM Serif Display', Georgia, serif;
  --sans:'Manrope', Arial, sans-serif;
}
*{box-sizing:border-box;margin:0;padding:0}
html,body{width:1200px;height:3893px;overflow:hidden}
body{background:var(--cream);font-family:var(--sans);color:var(--ink);position:relative}
.eyebrow{font-size:8px;font-weight:800;letter-spacing:.16em;text-transform:uppercase;color:var(--clay);display:flex;align-items:center;gap:8px}
.eyebrow::before{content:"";width:18px;height:1px;background:currentColor}
.serif{font-family:var(--serif);font-weight:400}
.btn{display:inline-flex;align-items:center;justify-content:center;height:30px;padding:0 14px;border-radius:16px;font-size:7.5px;font-weight:800;letter-spacing:.1em;text-transform:uppercase;text-decoration:none}
.arrow-link{display:flex;align-items:center;gap:8px;font-size:8px;font-weight:800;letter-spacing:.12em;text-transform:uppercase;color:var(--ink)}
.arrow-link span{width:20px;height:20px;border-radius:50%;border:1px solid var(--line);display:flex;align-items:center;justify-content:center;font-size:9px}

.site-nav{position:absolute;top:0;left:0;width:1200px;height:56px;background:var(--cream);border-bottom:1px solid var(--line)}
.brand{position:absolute;display:flex;align-items:center;gap:8px}
.brand-mark{width:22px;height:22px;border-radius:50%;border:1.5px solid currentColor}
.brand-name{font-family:var(--serif);font-size:13px;line-height:1}
.brand-sub{font-size:5.5px;font-weight:700;letter-spacing:.18em;margin-top:3px}
.site-nav .brand{left:219px;top:15px;color:var(--forest)}
.nav-links{position:absolute;left:456px;top:22px;display:flex;gap:19px;font-size:8.5px;font-weight:700}
.nav-cta{position:absolute;right:219px;top:14px;background:var(--forest);color:var(--white);height:28px;font-size:7.5px}

.hero{position:absolute;top:56px;left:0;width:1200px;height:536px;overflow:hidden}
.hero-photo{position:absolute;inset:0;background:linear-gradient(100deg,#3c3a33 0%,#6d685d 40%,#8d887c 65%,#7a7366 100%)}
.hero-shade{position:absolute;inset:0;background:linear-gradient(90deg,rgba(20,22,18,.55) 0%,rgba(20,22,18,.25) 55%,rgba(20,22,18,.1) 100%)}
.hero .eyebrow{position:absolute;left:219px;top:92px;color:#f1d9c8}
.hero h1{position:absolute;left:219px;top:110px;font-size:70px;line-height:72px;color:var(--white)}
.hero-lede{position:absolute;left:219px;top:276px;width:410px;font-size:12.5px;line-height:22px;color:#f2efe8}
.chips{position:absolute;display:flex;gap:7px}
.hero .chips{left:219px;top:336px}
.chip{height:22px;padding:0 9px;border-radius:12px;border:1px solid rgba(255,255,255,.45);background:rgba(255,255,255,.12);color:var(--white);font-size:7.5px;font-weight:700;display:flex;align-items:center}
.rating-card{position:absolute;left:836px;top:295px;width:145px;height:118px;border-radius:12px;background:rgba(40,40,34,.45);border:1px solid rgba(255,255,255,.25);padding:14px 12px;color:var(--white)}
.rating-card .score{font-family:var(--serif);font-size:30px;line-height:30px}
.rating-card .stars{position:absolute;right:14px;top:24px;font-size:6px;letter-spacing:2px;color:#e8c9a4}
.rating-card p{font-size:6.5px;line-height:10px;margin-top:6px;color:#ece7de}
.rating-card .pill{display:inline-block;margin-top:7px;background:var(--white);color:var(--ink);border-radius:8px;padding:3px 6px;font-size:5.5px;font-weight:800;letter-spacing:.08em}
.booking-bar{position:absolute;left:219px;top:456px;width:762px;height:60px;background:var(--white);border-radius:12px;padding:6px;display:flex;gap:6px;box-shadow:0 10px 30px rgba(0,0,0,.18)}
.field{border:1px solid var(--line);border-radius:8px;padding:9px 12px;position:relative}
.field label{display:block;font-size:5.5px;font-weight:800;letter-spacing:.14em;color:var(--muted)}
.field div{font-size:9px;font-weight:600;margin-top:6px}
.field svg{position:absolute;right:12px;top:24px}
.f-date{width:213px}.f-guests{width:130px}
.booking-bar .btn{flex:1;height:46px;border-radius:8px;background:var(--clay);color:var(--white);font-size:7.5px}
.hero-note{position:absolute;right:219px;top:522px;font-size:6px;color:#e2ddd2}

.stats{position:absolute;top:592px;left:0;width:1200px;height:73px;background:var(--forest)}
.stat{position:absolute;top:20px;color:var(--white)}
.stat b{display:block;font-family:var(--serif);font-weight:400;font-size:17px}
.stat small{display:block;font-size:6px;letter-spacing:.12em;color:#a9b9b0;margin-top:4px;font-weight:700}
.stat-div{position:absolute;top:18px;width:1px;height:38px;background:rgba(255,255,255,.15)}

.comfort{position:absolute;top:665px;left:0;width:1200px;height:555px;background:var(--cream)}
.comfort .eyebrow{position:absolute;left:219px;top:147px}
.comfort h2{position:absolute;left:219px;top:162px;font-size:48px;line-height:48px;width:360px}
.comfort .body{position:absolute;left:219px;top:321px;width:335px;font-size:10.5px;line-height:19px;color:var(--muted)}
.comfort .arrow-link{position:absolute;left:219px;top:398px}
.photo{position:absolute;overflow:hidden}
.comfort .photo-bed{left:688px;top:74px;width:293px;height:325px;border-radius:14px;background:linear-gradient(160deg,#d9d2c4 0%,#c8bfae 45%,#ece7dd 100%);box-shadow:0 18px 40px rgba(0,0,0,.12)}
.comfort .photo-house{left:600px;top:287px;width:175px;height:189px;border-radius:12px;border:5px solid var(--white);background:linear-gradient(180deg,#5b86b8 0%,#8faf7a 55%,#6e8a4d 100%);box-shadow:0 12px 30px rgba(0,0,0,.15)}
.comfort .caption{position:absolute;left:818px;top:418px;width:160px;font-size:7.5px;line-height:11px;color:var(--muted)}

.reasons{position:absolute;top:1220px;left:0;width:1200px;height:657px;background:var(--sand)}
.reasons .eyebrow{position:absolute;left:219px;top:82px}
.reasons h2{position:absolute;left:219px;top:97px;width:420px;font-size:48px;line-height:48px}
.reasons .intro{position:absolute;left:701px;top:170px;width:280px;font-size:10.5px;line-height:19px;color:var(--muted)}
.card{position:absolute;top:270px;height:311px;border-radius:12px;overflow:hidden}
.card .shade{position:absolute;inset:0;background:linear-gradient(180deg,rgba(0,0,0,0) 45%,rgba(15,25,20,.75) 100%)}
.card .txt{position:absolute;left:15px;right:14px;bottom:16px;color:var(--white)}
.card .num{font-size:6px;font-weight:800;letter-spacing:.14em;color:#e6d8c8}
.card h3{font-family:var(--serif);font-weight:400;font-size:26px;line-height:26px;margin:5px 0 5px}
.card p{font-size:7.5px;line-height:12px;color:#e8e4dc}
.card-1{left:219px;width:336px;background:linear-gradient(160deg,#c5bcae 0%,#9c9383 50%,#6f6658 100%)}
.card-2{left:567px;width:201px;background:linear-gradient(160deg,#ddd6c9 0%,#bdb3a3 55%,#8e8475 100%)}
.card-3{left:780px;width:201px;background:linear-gradient(170deg,#8fa36a 0%,#5e7442 50%,#4c5a36 100%)}

.location{position:absolute;top:1877px;left:0;width:1200px;height:586px;background:var(--cream)}
.location .photo-aerial{left:219px;top:95px;width:313px;height:393px;border-radius:16px;background:linear-gradient(160deg,#6f9fc7 0%,#3f78a2 35%,#5b7a5a 70%,#8a8a76 100%);box-shadow:0 18px 40px rgba(0,0,0,.15)}
.aerial-note{position:absolute;left:14px;bottom:16px;width:178px;background:rgba(255,255,255,.9);border-radius:10px;padding:11px 12px}
.aerial-note h4{font-family:var(--serif);font-weight:400;font-size:16px;line-height:17px}
.aerial-note p{font-size:6.5px;line-height:10px;color:var(--muted);margin-top:5px}
.location .eyebrow{position:absolute;left:567px;top:82px}
.location h2{position:absolute;left:567px;top:96px;width:414px;font-size:46px;line-height:47px}
.location .body{position:absolute;left:567px;top:201px;width:380px;font-size:10.5px;line-height:19px;color:var(--muted)}
.walk-list{position:absolute;left:567px;top:258px;width:414px;list-style:none;border-top:1px solid var(--line)}
.walk-list li{height:52px;border-bottom:1px solid var(--line);display:flex;align-items:center}
.walk-list .n{width:52px;font-family:var(--serif);font-size:16px;color:var(--clay)}
.walk-list .name{flex:1;font-size:8.5px;font-weight:700}
.walk-list .meta{font-size:7px;color:var(--muted)}
.location .footnote{position:absolute;left:567px;top:473px;font-size:6px;color:var(--muted)}
.location .arrow-link{position:absolute;left:567px;top:490px}

.reviews{position:absolute;top:2463px;left:0;width:1200px;height:387px;background:var(--forest)}
.reviews .big{position:absolute;left:219px;top:72px;font-size:58px;line-height:58px;color:var(--white)}
.reviews .stars{position:absolute;left:219px;top:140px;font-size:7px;letter-spacing:2px;color:#e8c9a4}
.reviews .sub{position:absolute;left:219px;top:155px;width:160px;font-size:7px;line-height:11px;color:#a9b9b0}
.reviews .vline{position:absolute;left:405px;top:75px;width:1px;height:236px;background:rgba(255,255,255,.15)}
.reviews blockquote{position:absolute;left:449px;top:88px;width:540px;font-family:var(--serif);font-size:38px;line-height:41px;color:var(--white)}
.reviews .fav{position:absolute;left:449px;top:256px;font-size:7px;color:#a9b9b0}
.reviews .chips{left:449px;top:290px;gap:6px}
.reviews .chip{height:20px;font-size:6.5px;font-weight:600;border-color:rgba(255,255,255,.25);background:transparent}

.direct{position:absolute;top:2850px;left:0;width:1200px;height:421px;background:var(--clay)}
.direct .eyebrow{position:absolute;left:219px;top:84px;color:#fbe9dd}
.direct h2{position:absolute;left:219px;top:100px;width:400px;font-size:47px;line-height:48px;color:var(--white)}
.direct .body{position:absolute;left:219px;top:254px;width:380px;font-size:10.5px;line-height:18px;color:#fbe9dd}
.direct .actions{position:absolute;left:219px;top:331px;display:flex;gap:9px}
.btn-light{background:var(--white);color:var(--ink)}
.btn-ghost{border:1px solid rgba(255,255,255,.55);color:var(--white)}
.perks{position:absolute;left:660px;top:122px;width:321px;display:grid;grid-template-columns:1fr 1fr;gap:8px}
.perk{height:80px;border-radius:8px;background:rgba(255,255,255,.08);border:1px solid rgba(255,255,255,.25);padding:11px 12px;color:var(--white)}
.tick{width:20px;height:20px;border-radius:50%;background:var(--white);display:flex;align-items:center;justify-content:center}
.perk h5{font-size:7.5px;font-weight:800;margin-top:9px}
.perk p{font-size:6px;line-height:9px;color:#f6dccd;margin-top:3px}

.cta{position:absolute;top:3271px;left:0;width:1200px;height:409px;background:var(--cream)}
.cta-card{position:absolute;left:219px;top:64px;width:762px;height:281px;border-radius:24px;background:var(--forest);overflow:hidden}
.cta-card .photo-front{right:0;top:0;width:430px;height:281px;background:linear-gradient(180deg,#6b8a9e 0%,#8e9a86 45%,#4e6d3d 100%)}
.cta-card .fade{position:absolute;right:220px;top:0;width:220px;height:281px;background:linear-gradient(90deg,var(--forest) 0%,rgba(29,59,48,0) 100%)}
.cta-card .eyebrow{position:absolute;left:41px;top:51px;color:#e8c9a4}
.cta-card h2{position:absolute;left:41px;top:67px;width:360px;font-size:44px;line-height:46px;color:var(--white)}
.cta-card .body{position:absolute;left:41px;top:162px;width:330px;font-size:10px;line-height:18px;color:#d5ddd8}
.cta-card .actions{position:absolute;left:41px;top:224px;display:flex;gap:8px}
.cta-card .btn-ghost{border-color:rgba(255,255,255,.35)}

.site-footer{position:absolute;top:3680px;left:0;width:1200px;height:213px;background:var(--forest-deep);color:var(--white)}
.site-footer .brand{left:219px;top:44px}
.footer-about{position:absolute;left:219px;top:94px;width:215px;font-size:7.5px;line-height:13px;color:#a9b9b0}
.f-col{position:absolute;top:48px}
.f-col h6{font-size:6px;font-weight:800;letter-spacing:.16em;color:#7f958a;margin-bottom:10px}
.f-col a{display:block;font-size:8px;color:#dfe6e2;text-decoration:none;margin-bottom:7px}
.footer-bar{position:absolute;left:219px;right:219px;top:176px;border-top:1px solid rgba(255,255,255,.1);padding-top:10px;display:flex;justify-content:space-between;font-size:6px;color:#7f958a}
</style>
</head>
<body>

<header class="site-nav">
  <div class="brand">
    <span class="brand-mark"></span>
    <div><div class="brand-name">Cedar Lantern Retreat</div><div class="brand-sub">BEND, OREGON</div></div>
  </div>
  <nav class="nav-links"><span>The House</span><span>Gallery</span><span>Explore Bend</span><span>Reviews</span><span>Book Direct</span></nav>
  <a class="btn nav-cta">Check availability &nbsp;→</a>
</header>

<section class="hero">
  <div class="hero-photo" role="img" aria-label="Bright open living room and kitchen with stone fireplace and bar stools"></div>
  <div class="hero-shade"></div>
  <div class="eyebrow">Tannery Row Quarter · Bend, Oregon</div>
  <h1 class="serif">Stay close.<br>Feel at home.</h1>
  <p class="hero-lede">A warm, pet-friendly 3-bedroom Bend retreat just minutes from the river, restaurants, shopping and summer concerts.</p>
  <div class="chips">
    <span class="chip">3 bedrooms</span><span class="chip">2 baths</span><span class="chip">Sleeps 6</span><span class="chip">Pet friendly</span><span class="chip">Fenced backyard</span>
  </div>
  <div class="rating-card">
    <div class="score">4.98</div>
    <div class="stars">★★★★★</div>
    <p>205 guest reviews with perfect 5.0 scores for cleanliness, location, check-in and communication.</p>
    <span class="pill">STAYVORA TOP 1%</span>
  </div>
  <form class="booking-bar">
    <div class="field f-date"><label>CHECK IN</label><div>mm / dd / yyyy</div>
      <svg width="9" height="9" viewBox="0 0 10 10"><rect x="1" y="2" width="8" height="7" fill="none" stroke="#1b2a24" stroke-width="1"/><line x1="1" y1="4" x2="9" y2="4" stroke="#1b2a24"/></svg></div>
    <div class="field f-date"><label>CHECK OUT</label><div>mm / dd / yyyy</div>
      <svg width="9" height="9" viewBox="0 0 10 10"><rect x="1" y="2" width="8" height="7" fill="none" stroke="#1b2a24" stroke-width="1"/><line x1="1" y1="4" x2="9" y2="4" stroke="#1b2a24"/></svg></div>
    <div class="field f-guests"><label>GUESTS</label><div>2 guests</div>
      <svg width="8" height="8" viewBox="0 0 10 10"><path d="M2 4l3 3 3-3" fill="none" stroke="#1b2a24" stroke-width="1.3"/></svg></div>
    <span class="btn">Check availability &nbsp;→</span>
  </form>
  <div class="hero-note">Preview mode · booking is not connected yet</div>
</section>

<section class="stats">
  <div class="stat" style="left:219px"><b>4.98★</b><small>205 GUEST REVIEWS</small></div>
  <div class="stat-div" style="left:412px"></div>
  <div class="stat" style="left:429px"><b>Top 1%</b><small>ELIGIBLE STAYVORA HOMES</small></div>
  <div class="stat-div" style="left:606px"></div>
  <div class="stat" style="left:623px"><b>~5 min</b><small>WALK TO TANNERY ROW</small></div>
  <div class="stat-div" style="left:799px"></div>
  <div class="stat" style="left:816px"><b>9 years</b><small>EXPERIENCED PRIME KEEPER</small></div>
</section>

<section class="comfort">
  <div class="eyebrow">A Bend stay that gets the details right</div>
  <h2 class="serif">Comfort first. Adventure right outside.</h2>
  <p class="body">Cedar Lantern Retreat gives you the best kind of Bend basecamp: quiet when you want to unwind, walkable when you want to head out, and thoughtfully equipped so the stay feels effortless.</p>
  <div class="arrow-link">Step inside the house <span>→</span></div>
  <div class="photo photo-bed" role="img" aria-label="Bright bedroom with chandelier and white bedding"></div>
  <div class="photo photo-house" role="img" aria-label="Front of the craftsman house with lawn and trees"></div>
  <p class="caption">Recently updated interiors, ultra-comfy beds and a fenced backyard built for lingering evenings.</p>
</section>

<section class="reasons">
  <div class="eyebrow">Three reasons guests return</div>
  <h2 class="serif">The rare mix of location, comfort &amp; calm.</h2>
  <p class="intro">Walk to Tannery Row, hear summer concerts from the covered porch, then come home to the privacy of a quiet cul-de-sac.</p>
  <article class="card card-1" role="img" aria-label="Living room with sectional sofa and stone fireplace">
    <div class="shade"></div>
    <div class="txt"><div class="num">01 · UNWIND</div><h3>Fenced backyard living</h3><p>A private, pet-friendly retreat with covered outdoor space and fire pit ambiance.</p></div>
  </article>
  <article class="card card-2" role="img" aria-label="Queen bedroom with chandelier">
    <div class="shade"></div>
    <div class="txt"><div class="num">02 · RECHARGE</div><h3>Sleep well</h3><p>One king and two queen beds with comfortable, recently refreshed rooms.</p></div>
  </article>
  <article class="card card-3" role="img" aria-label="Backyard garden with tall tree and fence">
    <div class="shade"></div>
    <div class="txt"><div class="num">03 · SETTLE IN</div><h3>Thoughtfully stocked</h3><p>A well-equipped kitchen, fireplace, Wi-Fi and the practical touches guests notice.</p></div>
  </article>
</section>

<section class="location">
  <div class="photo photo-aerial" role="img" aria-label="Aerial view of the riverfront shopping district in Bend">
    <div class="aerial-note"><h4>Bend at your doorstep.</h4><p>Tannery Row Quarter, river paths, dining, shopping and live music are all close by.</p></div>
  </div>
  <div class="eyebrow">Location is part of the stay</div>
  <h2 class="serif">Park the car. Walk into Bend.</h2>
  <p class="body">One of Cedar Lantern Retreat's strongest advantages is how much you can do without turning every outing into a drive.</p>
  <ul class="walk-list">
    <li><span class="n">05</span><span class="name">Tannery Row Quarter</span><span class="meta">minutes on foot*</span></li>
    <li><span class="n">08</span><span class="name">Larkspur Fields Pavilion</span><span class="meta">easy walk*</span></li>
    <li><span class="n">10</span><span class="name">Deschutes River paths</span><span class="meta">nearby*</span></li>
    <li><span class="n">∞</span><span class="name">Bend food, breweries &amp; outdoors</span><span class="meta">all around you</span></li>
  </ul>
  <p class="footnote">*Approximate walking times; routes vary.</p>
  <div class="arrow-link">Explore the neighborhood <span>→</span></div>
</section>

<section class="reviews">
  <div class="big serif">4.98</div>
  <div class="stars">★★★★★</div>
  <p class="sub">Based on 205 Stayvora reviews at the time this concept was prepared.</p>
  <div class="vline"></div>
  <blockquote>Guests consistently call out the location, spotless home, comfortable beds, thoughtful touches and backyard.</blockquote>
  <p class="fav">Stayvora Visitor Pick · Top 1% of eligible homes</p>
  <div class="chips">
    <span class="chip">Location 5.0</span><span class="chip">Cleanliness 5.0</span><span class="chip">Check-in 5.0</span><span class="chip">Communication 5.0</span><span class="chip">Pet friendly</span>
  </div>
</section>

<section class="direct">
  <div class="eyebrow">Book direct with confidence</div>
  <h2 class="serif">Same warm stay. A more direct way to reserve it.</h2>
  <p class="body">See availability, charges, cleaning fees, lodging taxes and your full reservation total before you pay. Card details are handled securely by Paylume —not stored on the Pressfold site.</p>
  <div class="actions"><a class="btn btn-light">Check availability</a><a class="btn btn-ghost">Questions? See FAQ</a></div>
  <div class="perks">
    <div class="perk"><span class="tick"><svg width="9" height="9" viewBox="0 0 10 10"><path d="M2 5l2 2 4-4" fill="none" stroke="#b96d4c" stroke-width="1.6"/></svg></span><h5>Live availability</h5><p>Calendar sync with Stayvora &amp; Hearthly via iCal.</p></div>
    <div class="perk"><span class="tick"><svg width="9" height="9" viewBox="0 0 10 10"><path d="M2 5l2 2 4-4" fill="none" stroke="#b96d4c" stroke-width="1.6"/></svg></span><h5>Transparent total</h5><p>Rates, fees and taxes before checkout.</p></div>
    <div class="perk"><span class="tick"><svg width="9" height="9" viewBox="0 0 10 10"><path d="M2 5l2 2 4-4" fill="none" stroke="#b96d4c" stroke-width="1.6"/></svg></span><h5>Secure card payment</h5><p>Paylume-hosted payment processing.</p></div>
    <div class="perk"><span class="tick"><svg width="9" height="9" viewBox="0 0 10 10"><path d="M2 5l2 2 4-4" fill="none" stroke="#b96d4c" stroke-width="1.6"/></svg></span><h5>Instant confirmation</h5><p>Automated reservation emails after booking.</p></div>
  </div>
</section>

<section class="cta">
  <div class="cta-card">
    <div class="photo photo-front" role="img" aria-label="Front of the house with porch, shrubs and tall pines"></div>
    <div class="fade"></div>
    <div class="eyebrow">Your Bend stay starts here</div>
    <h2 class="serif">Ready for Cedar Lantern Retreat?</h2>
    <p class="body">Choose your dates, check the complete price and reserve directly in a few simple steps.</p>
    <div class="actions"><a class="btn btn-light">Book direct</a><a class="btn btn-ghost">View photos</a></div>
  </div>
</section>

<footer class="site-footer">
  <div class="brand">
    <span class="brand-mark"></span>
    <div><div class="brand-name">Cedar Lantern Retreat</div><div class="brand-sub">BEND, OREGON</div></div>
  </div>
  <p class="footer-about">A warm, highly rated Bend home near the Tannery Row Quarter —made for comfortable stays, easy walks and direct bookings.</p>
  <div class="f-col" style="left:490px"><h6>STAY</h6><a>The House</a><a>Gallery</a><a>Guest Reviews</a></div>
  <div class="f-col" style="left:662px"><h6>PLAN</h6><a>Explore Bend</a><a>Book Direct</a><a>Contact &amp; FAQ</a></div>
  <div class="f-col" style="left:836px"><h6>CONFIDENCE</h6><a>Stayvora listing ↗</a><a>Secure payment</a><a>Calendar sync</a></div>
  <div class="footer-bar"><span>© 2026 Cedar Lantern Retreat. All rights reserved.</span><span>Independent direct booking website · Bend, Oregon</span></div>
</footer>

</body>
</html>
```